Microsite for a private healthcare provider

The design I need (PSD file) is for a company offering two services:
1. Recruitment of nurses
2. Provider a private health care: prenatal classes, vaccines for travellers
Here's a website we designed and we would like a similar style in terms of layout. Please note there will be about the same amount of content (text) http://lumivexstudio.ca/fr
Main menu with 4 sections:
Accueil |Agence de placement | Soins privés | Contact
Links to their social media accounts:
https://twitter.com/SoinsBrevalo
https://www.facebook.com/pages/SoinsBrevalo-Agence-de-placement-en-soins-de-sant%C3%A9/482913057264135
Contact details:
TÉL. (450) 555-0143
TÉLEC. (450) 555-0198
7186 boulevard Perrault, suite 1400
St-Hubert (Québec), J4X 1K3
Target Market(s)
Nurses looking for a job, Expecting women, People about to travel and seeking vaccines
Industry/Entity Type
Healthcare
Requirements
Must have
- 1- Must be responsive for mobiles and tablets
2 - Chirper feed
3 - Google maps at the end next to their contact details
4- Two contact forms:
Form for people to send in their resume.
The form title is: Postulez
Fields required:
Nom complet
Courriel
Téléphone
Années d'expérience (with drop down list: 1-2 ans, 3-5 ans, 5 ans et plus)
Choose file (possibility to attach a cv)
Message
Form for requesting information
Form title is: Demande d'informations
Fields are:
Nom complet
Téléphone
Courriel
Message
Nice to have
- Here are some images on Pixtura Foto the client likes, you can use for inspiration.
Agence de placement section:
File #40718253
File #6381947
File #5124086
File #8057291
File #30961472
File #27430685
File #45816037
Soins privés section:
File #36274519
File #49102853
File #31687240
File #25049716
File #43705128
File #38519602
File #29873154
File #7260835
File #34918657

```html
<!DOCTYPE html>
<html lang="fr">
<head>
<meta charset="utf-8">
<title>SoinsBrevalo – Soins de santé personnalisés</title>
<link rel="stylesheet" href="https://fonts.googleapis.com/css2?family=Open+Sans:wght@300;400;600;700&family=Dancing+Script:wght@600&display=swap">
<style>
:root{
  --green:#8fb416;
  --green-dark:#789a0e;
  --blue:#1b64b5;
  --sky:#1ba1e2;
  --sky-dark:#0d6ea3;
  --ink:#2b2b2b;
  --text:#6d6d6d;
  --muted:#9a9a9a;
  --line:#dcdcdc;
  --paper:#f4f4f4;
  --dark:#343434;
  --white:#ffffff;
}
*{box-sizing:border-box;margin:0;padding:0}
html,body{width:1200px;height:2433px;overflow:hidden}
body{position:relative;background:var(--white);font-family:"Open Sans",Arial,sans-serif;color:var(--text)}
.abs{position:absolute}

/* header */
.site-header{left:0;top:0;width:1200px;height:65px;background:var(--white);border-top:3px solid var(--green);box-shadow:0 1px 4px rgba(0,0,0,.12);z-index:3}
.brand{left:190px;top:12px;display:flex;align-items:center;gap:8px;font-weight:700;font-size:30px;color:var(--blue);letter-spacing:-.5px}
.brand-dot{width:12px;height:12px;border-radius:50%;background:var(--green);margin-top:14px}
.main-nav{left:579px;top:16px;display:flex;font-size:14px;font-weight:600;color:#555}
.main-nav a{color:inherit;text-decoration:none;padding:5px 12px;height:30px;display:block;line-height:20px;margin-right:8px}
.main-nav a.is-active{background:var(--green);color:var(--white);border-radius:2px}

/* hero */
.hero{left:0;top:65px;width:1200px;height:504px}
.hero-photo{left:0;top:0;width:1200px;height:504px;background:linear-gradient(90deg,#c6d2dc 0%,#e7ecf0 35%,#f3f5f7 55%,#c8d6e2 80%,#d8e1e9 100%)}
.apply-card{left:185px;top:70px;width:413px;height:364px;background:rgba(255,255,255,.97);border-radius:4px;box-shadow:0 2px 8px rgba(0,0,0,.15)}
.apply-rule{left:30px;top:43px;width:240px;height:2px;background:var(--green)}
.apply-title{right:30px;top:22px;font-size:24px;line-height:32px;font-weight:300;color:var(--green)}
.apply-divider{left:30px;top:58px;width:352px;height:1px;background:#e3e3e3}
.field-label{left:29px;font-size:12px;color:#555}
.field{left:168px;width:214px;height:26px;background:var(--white);border:1px solid var(--line);border-radius:2px}
.select-btn{right:0;top:0;width:27px;height:24px;background:#3a3a3a}
.browse{right:0;top:0;width:70px;height:24px;background:#3a3a3a;color:var(--white);font-size:10px;text-align:center;line-height:24px}
.btn-apply{left:281px;top:314px;width:101px;height:28px;background:linear-gradient(var(--green),var(--green-dark));color:var(--white);font-size:14px;text-align:center;line-height:28px;border-radius:2px}
.hero-heading{left:651px;top:195px;font-size:40px;font-weight:300;line-height:48px;color:var(--ink)}
.btn-blue{background:var(--blue);color:var(--white);font-weight:400;text-align:center;display:inline-block;border-radius:2px}
.hero-more{font-size:19px;line-height:36px;width:185px;margin-left:10px;vertical-align:4px}
.hero-sub{left:651px;top:356px;font-size:19px;line-height:28px;color:#333;width:395px}

/* recruit */
.recruit{left:0;top:569px;width:1200px;height:502px;background:var(--paper);border-bottom:1px solid #e3e3e3}
.section-title{font-size:40px;font-weight:300;line-height:44px;color:var(--ink)}
.recruit .section-title{left:185px;top:108px}
.recruit-cta{font-size:17px;line-height:33px;width:135px;margin-left:6px;vertical-align:4px}
.body-copy{font-size:13px;line-height:19.6px;color:var(--text)}
.recruit .body-copy{left:185px;top:208px;width:385px}
.btn-learn{left:187px;top:341px;width:101px;height:29px;background:var(--green);color:var(--white);font-size:11px;text-align:center;line-height:29px;border-radius:2px}
.photo-circle{border-radius:50%;border:6px solid var(--white);box-shadow:0 2px 6px rgba(0,0,0,.15)}
.photo-shadow{height:18px;border-radius:50%;background:radial-gradient(ellipse at center,rgba(0,0,0,.18),rgba(0,0,0,0) 70%)}

/* private care */
.private{left:0;top:1071px;width:1200px;height:497px;background:var(--paper)}
.private .section-title{left:624px;top:96px}
.service{left:624px;width:370px}
.service-name{font-size:19px;color:var(--green);font-weight:400}
.service-more{position:absolute;right:0;top:7px;width:55px;height:14px;font-size:9px;line-height:14px;color:var(--white);text-align:center}
.service .body-copy{margin-top:6px}

/* social */
.social{left:0;top:1568px;width:1200px;height:352px;background:var(--sky)}
.tweet-card{left:187px;top:24px;width:332px;height:273px;background:var(--white);border-radius:4px;overflow:hidden}
.tweet{position:relative;height:91px;border-bottom:1px solid #eee;padding:10px 60px 0 60px;font-size:11px;color:#444;line-height:15px}
.tweet:nth-child(2){background:#f7f9ef}
.tweet-avatar{position:absolute;left:12px;top:14px;width:36px;height:36px;background:var(--green);border-radius:3px}
.tweet-name{font-weight:600;color:#333}
.tweet-handle{color:var(--muted);font-weight:400}
.tweet-date{position:absolute;right:30px;top:10px;color:var(--muted);font-size:10px}
.tweet-expand{color:var(--muted);font-size:10px;margin-top:4px}
.tweet-actions{position:absolute;right:24px;bottom:10px;font-size:10px;color:var(--blue)}
.tweet-scroll{position:absolute;right:0;top:0;width:10px;height:273px;background:#eee}
.tweet-scroll i{display:block;width:10px;height:40px;background:var(--green)}
.tweet-tail{left:380px;top:294px}
.feed-label{left:240px;top:312px;font-family:"Dancing Script",cursive;font-size:22px;color:var(--white)}
.social-btn{left:626px;width:264px;height:45px;border:2px solid var(--white);color:var(--white);font-family:Georgia,serif;font-size:15px;font-weight:700;line-height:41px;text-align:center}
.social-divider{left:640px;top:169px}

/* info */
.info{left:0;top:1920px;width:1200px;height:144px;background:var(--dark)}
.info-tab{left:187px;top:0;width:84px;height:144px;background:var(--green)}
.info-tab span{position:absolute;left:42px;top:72px;transform:translate(-50%,-50%) rotate(-90deg);white-space:nowrap;font-size:17px;line-height:20px;color:var(--white);text-align:center}
.info-field{background:var(--white);border-radius:2px;height:24px;font-size:10px;color:#666;padding:5px 6px}
.btn-send{left:466px;top:87px;width:163px;height:24px;background:var(--green);color:var(--white);font-size:15px;line-height:24px;text-align:center;border-radius:2px}
.contact-title{left:747px;top:11px;font-size:23px;font-weight:300;color:var(--white)}
.contact-line{left:747px;font-size:13px;color:#ddd;line-height:16px;display:flex;gap:8px}

/* map + footer */
.map{left:0;top:2064px;width:1200px;height:314px;background:linear-gradient(135deg,#efebe4 0%,#f2efe9 50%,#e8ede0 100%)}
.footer-nav{left:187px;top:2390px;display:flex;gap:12px;font-size:10px;color:#888}
</style>
</head>
<body>

<header class="site-header abs">
  <div class="brand abs">SoinsBrevalo<span class="brand-dot"></span></div>
  <nav class="main-nav abs">
    <a class="is-active" href="#">Accueil</a>
    <a href="#">Agence de placement</a>
    <a href="#">Soins privés</a>
    <a href="#">Contact</a>
  </nav>
</header>

<section class="hero abs">
  <div class="hero-photo abs" role="img" aria-label="Photo floue d'une équipe de soignants souriants"></div>

  <form class="apply-card abs">
    <div class="apply-rule abs"></div>
    <div class="apply-title abs">Postulez</div>
    <div class="apply-divider abs"></div>

    <div class="field-label abs" style="top:86px">Nom complet</div>
    <div class="field abs" style="top:81px"></div>
    <div class="field-label abs" style="top:118px">Courriel</div>
    <div class="field abs" style="top:113px"></div>
    <div class="field-label abs" style="top:149px">Téléphone</div>
    <div class="field abs" style="top:144px"></div>
    <div class="field-label abs" style="top:181px">Années d'expérience</div>
    <div class="field abs" style="top:176px"><div class="select-btn abs"><svg width="27" height="24"><path d="M9 10h9l-4.5 5z" fill="#fff"/></svg></div></div>
    <div class="field-label abs" style="top:212px">Choisir le fichier</div>
    <div class="field abs" style="top:207px"><div class="browse abs">BROWSE</div></div>
    <div class="field-label abs" style="top:243px">Un message</div>
    <div class="field abs" style="top:239px;height:66px"></div>
    <div class="btn-apply abs">APPLY</div>
  </form>

  <h1 class="hero-heading abs">Soins de santé<br>personnalisés<br>au privé<span class="btn-blue hero-more">EN SAVOIR PLUS</span></h1>
  <p class="hero-sub abs">Make a difference and let your voice be heard. Find out more about joining.</p>
</section>

<section class="recruit abs">
  <h2 class="section-title abs">Nous recrutons des<br>infirmiers<span class="btn-blue recruit-cta">POSTULEZ</span></h2>
  <p class="body-copy abs">The Allied Care Nurses Council will be hosting a confer­ence to bring together recognized leaders and executives from a variety of organizations to share their most successful staffing ideas and proven strategies. Be there to leverage their latest thinking on innovative staffing models, leading practices, strategies and practical solutions.</p>
  <div class="btn-learn abs">LEARN MORE</div>
  <div class="photo-circle abs" style="left:643px;top:52px;width:370px;height:370px;background:linear-gradient(160deg,#e8eef4,#7aa6d6 60%,#2f6fb9)" role="img" aria-label="Photo de deux infirmiers souriants en uniforme, pouce levé"></div>
  <div class="photo-shadow abs" style="left:700px;top:436px;width:256px"></div>
</section>

<section class="private abs">
  <div class="photo-circle abs" style="left:187px;top:69px;width:370px;height:370px;background:linear-gradient(135deg,#eef1f3,#e9d8c8 55%,#d9b49a)" role="img" aria-label="Photo d'une soignante examinant un bébé avec un stéthoscope"></div>
  <div class="photo-shadow abs" style="left:244px;top:454px;width:256px"></div>

  <h2 class="section-title abs">Soins au privé</h2>

  <div class="service abs" style="top:166px">
    <h3 class="service-name">Vaccination De Voyage</h3>
    <span class="service-more" style="background:var(--green)">more →</span>
    <p class="body-copy">The Allied Care Nurses Council will be hosting a confer­ence to bring together recognized leaders and executives from a variety of organizations.</p>
  </div>
  <div class="abs" style="left:624px;top:269px;width:370px;height:1px;background:var(--line)"></div>
  <div class="service abs" style="top:296px">
    <h3 class="service-name">Soins Prénataux</h3>
    <span class="service-more" style="background:#bdbdbd">more →</span>
    <p class="body-copy">The Allied Care Nurses Council will be hosting a confer­ence to bring together recognized leaders and executives from a variety of organizations.</p>
  </div>
</section>

<section class="social abs">
  <div class="tweet-card abs">
    <article class="tweet">
      <span class="tweet-avatar"></span>
      <div><span class="tweet-name">SoinsBrevalo</span> <span class="tweet-handle">@SoinsBrevalo</span></div>
      <span class="tweet-date">13 Jun</span>
      <div>Grands besoins toujours présents pour l'Urgence! Nous attendons vos candidatures.</div>
      <div class="tweet-expand">Expand</div>
    </article>
    <article class="tweet">
      <span class="tweet-avatar"></span>
      <div><span class="tweet-name">SoinsBrevalo</span> <span class="tweet-handle">@SoinsBrevalo</span></div>
      <span class="tweet-date">13 Jun</span>
      <div>Grands besoins toujours présents pour l'Urgence! Nous attendons vos candidatures.</div>
      <div class="tweet-expand">Expand</div>
      <div class="tweet-actions">↩ Reply &nbsp; ⇄ Repost &nbsp; ••• More</div>
    </article>
    <article class="tweet">
      <span class="tweet-avatar"></span>
      <div><span class="tweet-name">SoinsBrevalo</span> <span class="tweet-handle">@SoinsBrevalo</span></div>
      <span class="tweet-date">13 Jun</span>
      <div>Grands besoins toujours présents pour l'Urgence! Nous attendons vos candidatures.</div>
      <div class="tweet-expand">Expand</div>
    </article>
    <div class="tweet-scroll"><i></i></div>
  </div>
  <svg class="tweet-tail abs" width="28" height="22"><path d="M0 0h28L10 22z" fill="#fff"/></svg>
  <div class="feed-label abs">Latest Posts</div>

  <div class="social-btn abs" style="top:84px">Follow@SoinsBrevalo</div>
  <svg class="social-divider abs" width="240" height="44" viewBox="0 0 240 44">
    <line x1="0" y1="22" x2="96" y2="22" stroke="#0d6ea3" stroke-width="1"/>
    <line x1="144" y1="22" x2="240" y2="22" stroke="#0d6ea3" stroke-width="1"/>
    <circle cx="120" cy="22" r="20" fill="#1590cc" stroke="#0d6ea3"/>
    <circle cx="120" cy="22" r="7" fill="none" stroke="#fff" stroke-width="2"/>
  </svg>
  <div class="social-btn abs" style="top:208px">Connect On Facepage</div>
</section>

<section class="info abs">
  <div class="info-tab abs"><span>Demande<br>d'informations</span></div>
  <div class="info-field abs" style="left:293px;top:30px;width:163px">Nom complet</div>
  <div class="info-field abs" style="left:293px;top:58px;width:163px">Téléphone</div>
  <div class="info-field abs" style="left:293px;top:87px;width:163px">Courriel</div>
  <div class="info-field abs" style="left:466px;top:30px;width:163px;height:48px">Un message</div>
  <div class="btn-send abs">SEND</div>

  <h3 class="contact-title abs">Contact Details</h3>
  <div class="contact-line abs" style="top:50px">
    <svg width="10" height="14" viewBox="0 0 10 14"><path d="M5 0a5 5 0 0 1 5 5c0 4-5 9-5 9S0 9 0 5a5 5 0 0 1 5-5z" fill="#fff"/><circle cx="5" cy="5" r="2" fill="#343434"/></svg>
    <span>7186 boulevard Perrault, suite 1400<br>St-Hubert (Québec), J4X 1K3</span>
  </div>
  <div class="contact-line abs" style="top:94px">
    <svg width="12" height="12" viewBox="0 0 12 12"><path d="M2 0l2.5 3-1.2 1.5a7 7 0 0 0 4.2 4.2L9 7.5 12 10l-1.5 2C5 12 0 7 0 1.5z" fill="#fff"/></svg>
    <span>(450) 555-0143</span>
  </div>
  <div class="contact-line abs" style="top:113px">
    <svg width="12" height="12" viewBox="0 0 12 12"><rect x="0" y="4" width="12" height="8" rx="1" fill="#fff"/><rect x="3" y="0" width="6" height="5" fill="#fff"/><rect x="3" y="6" width="6" height="1.5" fill="#343434"/></svg>
    <span>(450) 555-0198</span>
  </div>
</section>

<div class="map abs" role="img" aria-label="Carte du quartier autour du bureau de St-Hubert avec repère d'emplacement"></div>

<nav class="footer-nav abs">
  <span>Accueil</span><span>Agence de placement</span><span>Soins privés</span><span>Contact</span>
</nav>

</body>
</html>
```